Daily Deals Website Needs a Landing Page (Home Page will act as the landing page)

We need a landing page for a daily deals website that will act as the home page. We have attached the wire frame and logo for reference. Open to creative ideas and suggestions as long as the main elements of the wireframe are incorporated in the design. Need a very simplistic design approach like Vorplex's search page. (www.vorplex.com) . Very clean and distinct CTA's.

Target Market(s)

Customers looking for deals on everyday use items

Font styles to use
Sans Serif

Requirements
Must have
• clean design, lots of white space and strong CTA .
Nice to have
• need a clean design overall. Strong CTA
Should not have
• Cluttered look. Too many colors, keep it simple

```html
<!DOCTYPE html>
<html lang="en">
<head>
<meta charset="UTF-8">
<title>Dealnest – Daily Deals</title>
<link href="https://fonts.googleapis.com/css2?family=Poppins:wght@300;400;500;600&family=Open+Sans:wght@400;600&display=swap" rel="stylesheet">
<style>
  :root {
    --navy: #1f3399;
    --green: #6cc04a;
    --ink: #333333;
    --muted: #6f7380;
    --page: #f0f1f5;
    --hero-light: #fbfbfd;
    --card: #f6f7fb;
    --white: #ffffff;
    --img-green: #e6eae3;
    --img-grey: #e0e0e9;
    --icon: #a8b4c0;
  }
  * { box-sizing: border-box; margin: 0; padding: 0; }
  html, body { width: 1200px; height: 1094px; overflow: hidden; }
  body {
    position: relative;
    background: var(--page);
    font-family: "Poppins", sans-serif;
    color: var(--ink);
  }
  .hero-bg {
    position: absolute; left: 0; top: 0; width: 1200px; height: 669px;
    background: radial-gradient(ellipse 520px 420px at 600px 260px, var(--hero-light), #f2f2f7 100%);
  }
  .brand {
    position: absolute; top: 40px; left: 0; width: 1200px;
    display: flex; justify-content: center; align-items: center; gap: 10px;
  }
  .brand-mark { width: 16px; height: 16px; background: var(--green); }
  .brand-name {
    font-weight: 600; font-size: 40px; color: var(--navy); letter-spacing: 0.5px; line-height: 1;
  }
  .intro { position: absolute; top: 164px; left: 0; width: 1200px; text-align: center; }
  .eyebrow { font-size: 10px; font-weight: 500; color: var(--navy); letter-spacing: -0.2px; }
  .headline { margin-top: 6px; font-size: 27px; line-height: 35px; font-weight: 500; letter-spacing: -0.4px; }
  .headline .light { font-weight: 300; }
  .headline strong { font-weight: 600; }
  .signup {
    position: absolute; left: 401px; width: 398px; height: 44px;
    background: var(--white); border-radius: 22px;
    box-shadow: 0 4px 14px rgba(40, 50, 90, 0.06);
    display: flex; align-items: center; justify-content: space-between;
    padding: 0 5px 0 23px;
  }
  .signup-top { top: 299px; }
  .signup-bottom { top: 873px; }
  .signup input {
    border: none; outline: none; background: transparent;
    font-family: "Open Sans", sans-serif; font-size: 11px; color: var(--muted); width: 200px;
  }
  .signup input::placeholder { color: var(--muted); }
  .signup-btn {
    width: 154px; height: 34px; border: none; border-radius: 17px;
    font-family: "Open Sans", sans-serif; font-weight: 600; font-size: 12px; color: var(--white);
  }
  .btn-green { background: var(--green); }
  .btn-navy { background: var(--navy); }
  .deal-title {
    position: absolute; width: 338px; text-align: center;
    font-size: 17px; font-weight: 400; letter-spacing: -0.2px;
  }
  .deal-card {
    position: absolute; top: 454px; width: 338px; height: 345px;
    background: var(--card); padding: 13px 14px 0;
  }
  .deal-image {
    width: 310px; height: 203px; border-radius: 6px;
    display: flex; align-items: center; justify-content: center;
  }
  .deal-image.green { background: var(--img-green); }
  .deal-image.grey { background: var(--img-grey); }
  .deal-text {
    margin-top: 16px; text-align: center; font-size: 11.5px; line-height: 17px; font-weight: 300; color: var(--ink);
  }
  .deal-btn {
    display: block; margin: 13px auto 0; width: 104px; height: 31px; border: none; border-radius: 2px;
    font-family: "Open Sans", sans-serif; font-weight: 600; font-size: 11px; color: var(--white);
    box-shadow: 0 8px 18px rgba(40, 50, 90, 0.12);
  }
  .footer {
    position: absolute; left: 0; top: 1037px; width: 1200px; height: 57px;
    background: var(--white); text-align: center; padding-top: 16px;
    font-size: 11px; color: var(--muted);
  }
</style>
</head>
<body>
  <div class="hero-bg"></div>

  <header class="brand">
    <span class="brand-mark"></span>
    <span class="brand-name">Dealnest</span>
  </header>

  <section class="intro">
    <p class="eyebrow">Lorem Ipsum is simply</p>
    <h1 class="headline">Lorem Ipsum is simply dummy<br><span class="light">text of the printing,</span> <strong>ypesetting.</strong></h1>
  </section>

  <form class="signup signup-top">
    <input type="email" placeholder="Enter your Email ID">
    <button type="button" class="signup-btn btn-green">Daily Emails Sign up</button>
  </form>

  <h2 class="deal-title" style="left:247px; top:414px;">Featured Deal of the Day</h2>
  <h2 class="deal-title" style="left:615px; top:417px;">Promoted Deal of the Day</h2>

  <article class="deal-card" style="left:247px;">
    <div class="deal-image green" role="img" aria-label="Featured deal product photo">
      <svg width="32" height="32" viewBox="0 0 32 32" aria-hidden="true" fill="none" stroke="var(--icon)" stroke-width="1.6">
        <rect x="1" y="1" width="30" height="30" rx="3"/>
        <circle cx="10" cy="9" r="3.2"/>
        <path d="M1 24 L10 16 L16 21 L23 13 L31 21"/>
      </svg>
    </div>
    <p class="deal-text">Lorem Ipsum is simply dummy text of the<br>printing and typesetting industry</p>
    <button type="button" class="deal-btn btn-green">Click Here</button>
  </article>

  <article class="deal-card" style="left:615px;">
    <div class="deal-image grey" role="img" aria-label="Promoted deal product photo">
      <svg width="32" height="32" viewBox="0 0 32 32" aria-hidden="true" fill="none" stroke="var(--icon)" stroke-width="1.6">
        <rect x="1" y="1" width="30" height="30" rx="3"/>
        <circle cx="10" cy="9" r="3.2"/>
        <path d="M1 24 L10 16 L16 21 L23 13 L31 21"/>
      </svg>
    </div>
    <p class="deal-text">Lorem Ipsum is simply dummy text of the<br>printing and typesetting industry</p>
    <button type="button" class="deal-btn btn-navy">Click Here</button>
  </article>

  <form class="signup signup-bottom">
    <input type="email" placeholder="Enter your Email ID">
    <button type="button" class="signup-btn btn-navy">Daily Emails Sign up</button>
  </form>

  <footer class="footer">© 2021 dealnest. All Rights are Reserved.</footer>
</body>
</html>
```